Kestrel Gardenworks Business Card

An eye catching, yet simple business card that includes;

1. our logo
2. office phone - 5083172946
3. email - kestrelgardenworks@mailbrook.com
4. website - www.kestrelgardenworks.com
5. instagram - @kestrelgardenworksnv

```html
<!DOCTYPE html>
<html lang="en">
<head>
<meta charset="utf-8">
<title>Kestrel Gardenworks Business Card</title>
<link href="https://fonts.googleapis.com/css2?family=Lato:wght@400;700;900&family=Dancing+Script:wght@500&display=swap" rel="stylesheet">
<style>
  :root {
    --bg: #2b2b2b;
    --brown: #9c5d2a;
    --white: #ffffff;
    --ink: #1c1c1c;
    --grey: #5a5a5a;
  }
  * { box-sizing: border-box; margin: 0; padding: 0; }
  html, body { width: 1200px; height: 875px; overflow: hidden; }
  body {
    background: var(--bg);
    font-family: "Lato", sans-serif;
    position: relative;
  }
  .card {
    position: absolute;
    top: 283px;
    width: 540px;
    height: 309px;
    border-radius: 16px;
    overflow: hidden;
  }
  .card-front { left: 40px; background: var(--brown); color: var(--white); }
  .card-back { left: 620px; background: var(--white); color: var(--ink); }

  .front-name {
    position: absolute; left: 0; right: 0; top: 86px;
    text-align: center;
    font-weight: 900; font-size: 44px; line-height: 1.05;
    text-transform: uppercase; letter-spacing: 2px;
  }
  .tagline {
    position: absolute; left: 0; right: 0; bottom: 42px;
    text-align: center;
    font-family: "Dancing Script", cursive; font-size: 26px;
  }

  .back-logo {
    position: absolute; right: 30px; top: 28px;
    text-align: right;
    font-weight: 900; font-size: 24px; line-height: 1.05;
    text-transform: uppercase; letter-spacing: 1px;
    color: var(--brown);
  }
  .person { position: absolute; left: 30px; top: 102px; }
  .person-name { font-weight: 700; font-size: 28px; color: var(--brown); text-transform: uppercase; line-height: 1; }
  .person-role { font-size: 15px; margin-top: 5px; }
  .divider {
    position: absolute; left: 30px; right: 30px; top: 160px;
    height: 1px; background: var(--brown);
  }

  .contacts { position: absolute; left: 30px; top: 174px; list-style: none; }
  .contacts li { display: flex; align-items: center; gap: 10px; font-size: 14px; color: var(--grey); line-height: 25px; }
  .contacts svg { width: 12px; height: 12px; fill: none; stroke: var(--brown); stroke-width: 1.6; }

  .address {
    position: absolute; right: 30px; top: 174px;
    text-align: right; font-size: 14px; font-style: normal;
    color: var(--grey); line-height: 21px;
  }
  .address .company { color: var(--brown); }
</style>
</head>
<body>
  <section class="card card-front">
    <div class="front-name">Kestrel<br>Gardenworks</div>
    <p class="tagline">Where tidy green spaces take shape every day!</p>
  </section>

  <section class="card card-back">
    <div class="back-logo">Kestrel<br>Gardenworks</div>

    <div class="person">
      <div class="person-name">Marlo Pennick</div>
      <div class="person-role">Creative Director</div>
    </div>

    <div class="divider"></div>

    <ul class="contacts">
      <li><svg viewBox="0 0 12 12"><path d="M2 1h2l1 3-1.5 1a6 6 0 0 0 3.5 3.5L8 7l3 1v2a1 1 0 0 1-1 1A9 9 0 0 1 1 2a1 1 0 0 1 1-1z"/></svg>5083172946</li>
      <li><svg viewBox="0 0 12 12"><rect x="1" y="2.5" width="10" height="7"/><path d="M1 2.5l5 4 5-4"/></svg>kestrelgardenworks@mailbrook.com</li>
      <li><svg viewBox="0 0 12 12"><circle cx="6" cy="6" r="5"/><path d="M1 6h10M6 1c-2 2.5-2 7.5 0 10M6 1c2 2.5 2 7.5 0 10"/></svg>www.kestrelgardenworks.com</li>
      <li><svg viewBox="0 0 12 12"><rect x="1" y="1" width="10" height="10" rx="3"/><circle cx="6" cy="6" r="2.3"/></svg>@kestrelgardenworksnv</li>
    </ul>

    <address class="address">
      <span class="company">Kestrel Gardenworks</span><br>
      3318 Fenwick Ln<br>
      Brookhaven, NV, 89052<br>
      United States
    </address>
  </section>
</body>
</html>
```